Roving Beam Arena

Information can be taken and lifted from the professional website mobilelasertags.comI am a new start up in my area. I have no designs or logos of my own.The service we offer is Laser Tag using the Photon Dash brand. I would like their logo on my card. On the card I need my contact info, the different services we offer, with a focus on Law Enforcement / Military Training, Party, Celebration, Schools, Weekend and Holidays. I am open to any color and back grounds. It needs to have our rates listed as well as our service areas: Serving South Georgia Brantley, Camden, Charlton, Glynn, Pierce, Ware, McintoshServing North Florida Baker, Clay, Duval, Nassau, St. Johns, Union, Putnum, Flagler, AlachuaYou can find black and white images on the website.

Industry/Entity Type

It Professional

Contact Information for Business Card

Benjamin Hayward912-227-7195mobilelasertags.cominfo@rovingbeamarena.example

Requirements
Must have
• Service areas, rates, and events catered to.

```html
<!DOCTYPE html>
<html lang="en">
<head>
<meta charset="utf-8">
<title>Roving Beam Arena – Business Card</title>
<link href="https://fonts.googleapis.com/css2?family=Oswald:wght@400;600;700&display=swap" rel="stylesheet">
<style>
  :root {
    --stage: #e4e4e4;
    --card-dark: #2e2e30;
    --band-red: #c0251f;
    --band-red-deep: #8e1512;
    --band-red-light: #de3a2c;
    --edge-light: #ff8a7a;
    --text-white: #f4f4f4;
    --text-soft: #d6d6d6;
    --logo-cream: #efe6d2;
    --badge-fill: #e9d6d3;
    --map-fill: #e8e8e8;
  }
  * { box-sizing: border-box; margin: 0; padding: 0; }
  html, body { width: 1200px; height: 750px; overflow: hidden; }
  body {
    background: var(--stage);
    font-family: "Oswald", "Arial Narrow", sans-serif;
    display: flex; align-items: center; justify-content: center; gap: 20px;
  }
  .card {
    position: relative; width: 570px; height: 330px;
    background: var(--card-dark); border-radius: 22px; overflow: hidden;
    color: var(--text-white);
    box-shadow: 0 6px 18px rgba(0,0,0,.18);
  }
  .red-band {
    position: absolute; left: 0; right: 0;
    background: linear-gradient(100deg, var(--band-red-light), var(--band-red) 45%, var(--band-red-deep));
    border-top: 2px solid var(--edge-light);
    border-bottom: 2px solid var(--edge-light);
  }
  /* front */
  .card-front .red-band { top: 78px; height: 174px; }
  .front-logo {
    position: absolute; inset: 0;
    display: flex; align-items: center; justify-content: center; gap: 12px;
  }
  .logo-dot { width: 26px; height: 26px; border-radius: 50%; background: var(--logo-cream); }
  .logo-name {
    font-weight: 700; font-size: 46px; letter-spacing: 1px;
    text-transform: uppercase; color: var(--logo-cream);
  }
  /* back */
  .card-back .red-band { top: 20px; height: 78px; }
  .badge {
    position: absolute; top: 9px; width: 56px; height: 56px; border-radius: 50%;
    background: var(--badge-fill); border: 2px solid #fff;
  }
  .back-logo {
    position: absolute; left: 150px; right: 150px; top: 10px;
    text-align: center;
  }
  .back-logo .logo-name { font-size: 26px; line-height: 1.1; }
  .web-line { font-size: 11px; letter-spacing: 1.5px; color: var(--text-white); margin-top: 3px; }
  .holder-name {
    position: absolute; left: 24px; top: 110px; width: 256px;
    font-weight: 700; font-size: 21px; letter-spacing: 2px; text-align: center;
    border-bottom: 1px solid var(--text-soft); padding-bottom: 4px; white-space: nowrap;
  }
  .contact-list {
    position: absolute; left: 294px; top: 110px; width: 156px; list-style: none;
    font-size: 8.5px; letter-spacing: .3px; color: var(--text-white);
  }
  .contact-list li { display: flex; align-items: center; gap: 5px; margin-bottom: 5px; white-space: nowrap; }
  .contact-list svg { width: 11px; height: 11px; flex: none; }
  .service-areas { position: absolute; right: 18px; top: 106px; width: 92px; }
  .service-areas h3 { font-size: 10px; font-weight: 600; letter-spacing: 1px; margin-bottom: 4px; white-space: nowrap; }
  .area-map { height: 74px; background: linear-gradient(135deg, var(--map-fill), #c9c9c9); border: 1px solid #fff; }
  .rates { position: absolute; left: 24px; top: 176px; width: 290px; }
  .rates h2 { font-size: 13px; font-weight: 600; letter-spacing: 1px; margin-bottom: 6px; white-space: nowrap; }
  .rates ul { list-style: none; font-size: 9px; letter-spacing: .3px; color: var(--text-soft); }
  .rates li { display: flex; gap: 7px; align-items: center; margin-bottom: 5px; white-space: nowrap; }
  .rates li::before { content: ""; width: 5px; height: 5px; border-radius: 50%; background: var(--text-white); flex: none; }
  .events {
    position: absolute; left: 326px; right: 18px; top: 206px;
    font-size: 9px; letter-spacing: .4px; line-height: 1.8; text-align: center; color: var(--text-white);
  }
  .events span { display: block; white-space: nowrap; }
</style>
</head>
<body>
  <section class="card card-front">
    <div class="red-band">
      <div class="front-logo">
        <span class="logo-dot"></span>
        <span class="logo-name">Photon Dash</span>
      </div>
    </div>
  </section>

  <section class="card card-back">
    <div class="red-band">
      <div class="badge" style="left:18px" role="img" aria-label="Badge illustration: laser tag player"></div>
      <div class="badge" style="left:84px" role="img" aria-label="Badge illustration: military"></div>
      <div class="back-logo">
        <div class="logo-name">Photon Dash</div>
        <div class="web-line">WWW.ROVINGBEAMARENA.EXAMPLE</div>
      </div>
      <div class="badge" style="right:84px" role="img" aria-label="Badge illustration: celebration group"></div>
      <div class="badge" style="right:18px" role="img" aria-label="Badge illustration: law enforcement"></div>
    </div>

    <div class="holder-name">DESMOND WHITCOMBE</div>

    <ul class="contact-list">
      <li><svg viewBox="0 0 12 12"><circle cx="6" cy="6" r="5.5" fill="none" stroke="#fff"/><path d="M4 3.2l1 1.2-.6.8c.4.9 1 1.5 1.9 1.9l.8-.6 1.2 1-.6 1C5.7 8.3 3.7 6.3 3.2 4.2z" fill="#fff"/></svg>912-555-0148</li>
      <li><svg viewBox="0 0 12 12"><circle cx="6" cy="6" r="5.5" fill="none" stroke="#fff"/><rect x="3" y="4" width="6" height="4" fill="none" stroke="#fff" stroke-width=".8"/><path d="M3 4l3 2.3L9 4" fill="none" stroke="#fff" stroke-width=".8"/></svg>INFO@ROVINGBEAMARENA.EXAMPLE</li>
      <li><svg viewBox="0 0 12 12"><circle cx="6" cy="6" r="5.5" fill="none" stroke="#fff"/><circle cx="6" cy="6" r="3" fill="none" stroke="#fff" stroke-width=".8"/><path d="M3 6h6M6 3v6" stroke="#fff" stroke-width=".6"/></svg>ROVINGBEAMARENA.EXAMPLE</li>
    </ul>

    <div class="service-areas">
      <h3>SERVICE AREAS</h3>
      <div class="area-map" role="img" aria-label="County map of South Georgia and North Florida service areas"></div>
    </div>

    <div class="rates">
      <h2>PRICES &amp; RATES FOR LASER TAG GAMES</h2>
      <ul>
        <li>2 HOUR TIME BLOCKS PRO RATED</li>
        <li>MINIMUM 2 UNIT RENTAL (UNIT IS VEST AND PHASER COMBINATION)</li>
        <li>$10 / HOUR PER UNIT.</li>
        <li>UNLIMITED GAMES AND FUN DURING THE RENTAL TIME.</li>
      </ul>
    </div>

    <p class="events">
      <span>BIRTHDAY • HOLIDAY • CORPORATE EVENTS PARTIES</span>
      <span>WEEKEND FUN • MILITARY</span>
      <span>LAW ENFORCEMENT • SCHOOLS • CHARITY • FUND RAISING</span>
    </p>
  </section>
</body>
</html>
```